Poster announcing University Web Analytics talk

We need a poster to announce an upcoming talk on Web Analytics at the local University. The event is addressed to final year students (mostly in Informatic Engineering, although other majors are wellcomed as well) who may be interested in specializing in this rising field.

The poster should present a brief list of the points we'll be addressing, as well as the place and time of the meeting. Also, it must feature our company logo (check the uploads section to find it) and our website url: http://www.brasslanternworks.net.

Texts for the poster:

Headline: "Get specialized in Web & Mobile Analytics"

Topics that will be covered:
- Introduction to Analytics, market, work opportunities
- Know the basics of an Analytics project: planning, phases, implementation
- Job bank: bring your CV!

Event information: "Thursday 20th June at the Escuela de Sistemas, Instituto Pelayo Norte". [A space to fill with the time must be provided here]

However, we'll be translating all the text to Spanish later, so we'll need a file where we can modify the text layers.
Updates

Thanks to all of you, we're receiving so many excellent works!

We had missed to include some important information on the brief - we didn't say anything about the colors, and we have been getting some designs based in dark colors. Now, it doesn't matter what colors you use, but we'd like better a brighter design (no matter if the color combination is more playful or either rather serious). This is going to be a free talk addressed to last year students, so we want to transmit a feeling of an interesting, easy and entertaining afternoon.

I hope these comments are helpful, please reach me with any question or comment. 

Thanks a lot again!
Nuria 
BL team

Target Market(s)

Final year students and graduates.

Industry/Entity Type

Bank

Requirements
Must have
• Design must be submitted in vector format, preferably .psd. We must be able to modify the text layers. Our logo (check the files section) and website url (http://www.brasslanternworks.net) must be included
Nice to have
• Illustrations making reference to Analytics (charts, statistics, code) and/or the internet will be a plus!

```html
<!DOCTYPE html>
<html lang="en">
<head>
<meta charset="utf-8">
<title>Get specialized in Web &amp; Mobile Analytics</title>
<link rel="stylesheet" href="https://fonts.googleapis.com/css2?family=Roboto+Condensed:wght@400;700&display=swap">
<style>
  :root {
    --bg-side: #e4e5e8;
    --bg-main: #f2f3f5;
    --ink: #5b5b5d;
    --ink-soft: #6d6e70;
    --blue: #3d6db3;
    --blue-dark: #24477f;
    --navy: #1e3a78;
    --navy-dark: #122552;
    --forest: #207a3d;
    --forest-dark: #14552a;
    --green: #3aa648;
    --green-dark: #267a32;
    --slate: #4a4a4c;
    --slate-dark: #2f2f31;
    --white: #ffffff;
  }
  * { margin: 0; padding: 0; box-sizing: border-box; }
  html, body { width: 849px; height: 1200px; overflow: hidden; }
  body { background: var(--bg-main); font-family: "Roboto Condensed", Arial, sans-serif; }
  .poster {
    position: relative;
    width: 849px;
    height: 1200px;
    overflow: hidden;
    background: linear-gradient(90deg, var(--bg-side) 0, var(--bg-side) 265px, #f7f7f8 265px, var(--bg-main) 849px);
  }
  .ribbons { position: absolute; left: 0; top: 0; }
  .headline {
    position: absolute;
    left: 302px;
    top: 172px;
    color: var(--ink);
    font-weight: 700;
    font-size: 44px;
    line-height: 62px;
    letter-spacing: -0.3px;
  }
  .topic {
    position: absolute;
    left: 311px;
    color: var(--white);
    font-weight: 700;
    font-size: 17px;
    line-height: 23px;
  }
  .topic--intro { top: 322px; }
  .topic--basics { top: 421px; }
  .topic--plan { top: 500px; }
  .topic--jobs { top: 584px; }
  .topic--cv { top: 664px; left: 304px; font-size: 29px; line-height: 40px; }
  .event {
    position: absolute;
    left: 303px;
    top: 797px;
    color: var(--ink-soft);
    font-weight: 700;
    font-size: 20px;
    line-height: 25px;
  }
  .brand {
    position: absolute;
    left: 303px;
    top: 910px;
    display: flex;
    align-items: center;
    gap: 12px;
  }
  .brand__mark { width: 40px; height: 40px; background: var(--forest); }
  .brand__name {
    color: var(--navy);
    font-weight: 700;
    font-size: 30px;
    line-height: 1;
  }
  .website {
    position: absolute;
    left: 303px;
    top: 990px;
    color: var(--ink-soft);
    font-weight: 700;
    font-size: 21px;
  }
</style>
</head>
<body>
<main class="poster">
  <svg class="ribbons" width="849" height="1200" viewBox="0 0 849 1200" aria-hidden="true">
    <defs>
      <linearGradient id="fold-blue" x1="0" x2="1"><stop offset="0" stop-color="var(--blue)"/><stop offset="1" stop-color="var(--blue-dark)"/></linearGradient>
      <linearGradient id="fold-navy" x1="0" x2="1"><stop offset="0" stop-color="var(--navy)"/><stop offset="1" stop-color="var(--navy-dark)"/></linearGradient>
      <linearGradient id="fold-forest" x1="0" x2="1"><stop offset="0" stop-color="var(--forest)"/><stop offset="1" stop-color="var(--forest-dark)"/></linearGradient>
      <linearGradient id="fold-green" x1="0" x2="1"><stop offset="0" stop-color="var(--green)"/><stop offset="1" stop-color="var(--green-dark)"/></linearGradient>
      <linearGradient id="fold-slate" x1="0" x2="1"><stop offset="0" stop-color="var(--slate)"/><stop offset="1" stop-color="var(--slate-dark)"/></linearGradient>
    </defs>
    <!-- fanned tails -->
    <polygon class="ribbon-tail" points="0,201 265,303 265,392 0,356" fill="url(#fold-blue)"/>
    <polygon class="ribbon-tail" points="0,356 265,396 265,470 0,490" fill="url(#fold-navy)"/>
    <polygon class="ribbon-tail" points="0,490 265,474 265,550 0,626" fill="url(#fold-forest)"/>
    <polygon class="ribbon-tail" points="0,626 265,553 265,639 0,750" fill="url(#fold-green)"/>
    <polygon class="ribbon-tail" points="0,750 265,644 265,730 0,935" fill="url(#fold-slate)"/>
    <!-- arrow heads -->
    <polygon class="ribbon-arrow" points="265,303 684,303 705,347 684,392 265,392" fill="var(--blue-dark)"/>
    <polygon class="ribbon-arrow" points="265,396 592,396 610,433 592,470 265,470" fill="var(--navy)"/>
    <polygon class="ribbon-arrow" points="265,474 616,474 635,512 616,550 265,550" fill="var(--forest)"/>
    <polygon class="ribbon-arrow" points="265,553 671,553 692,596 671,639 265,639" fill="var(--green)"/>
    <polygon class="ribbon-arrow" points="265,644 538,644 557,687 538,730 265,730" fill="var(--slate)"/>
  </svg>

  <h1 class="headline">Get specialized in<br>Web &amp; Mobile Analytics</h1>

  <p class="topic topic--intro">Introduction to Analytics, market,<br>work opportunities</p>
  <p class="topic topic--basics">Know the basics of an Analytics<br>project</p>
  <p class="topic topic--plan">Planning, phases, implementation</p>
  <p class="topic topic--jobs">Job bank</p>
  <p class="topic topic--cv">bring your CV!</p>

  <p class="event">Thursday 20th June at the Escuela de Sistemas,<br>Instituto Pelayo Norte<br>Time here</p>

  <div class="brand">
    <span class="brand__mark"></span>
    <span class="brand__name">Brass Lantern Works</span>
  </div>

  <p class="website">www.brasslanternworks.net</p>
</main>
</body>
</html>
```